Company web site

Looking for a full responsive(mobile friendly) wordpress implementation

Some material is in the website -- brivanta.examplesite.test

But looking for a template more consistent with the logo design, and more future looking.

Target Market(s)

Enterprise Clients

Industry/Entity Type

It Company

Font styles to use
Sans Serif

Colors
33a6d7
0255a3
0455a3
cfdeed
85abd2
3176b5

Requirements
Must have
• about, contact information, partner page, success stories, customer testimonials. links to social presence.
• pricing information

```html
<!DOCTYPE html>
<html lang="en">
<head>
<meta charset="utf-8">
<title>Brivanta — Home</title>
<link href="https://fonts.googleapis.com/css2?family=Jost:wght@300;400;500;600&display=swap" rel="stylesheet">
<style>
  :root{
    --stage:#000000;
    --header-dark:#0b0f16;
    --header-mid:#151c27;
    --brand-cyan:#33a6d7;
    --brand-blue:#0255a3;
    --sky-pale:#cfdeed;
    --sky-soft:#85abd2;
    --sky-bright:#8fcdec;
    --tab-fill:#3a3f47;
    --tab-active:#6f8aa6;
    --ink:#111418;
    --paper:#ffffff;
    --rule:#8a8f96;
    --bubble:#2a2e34;
  }
  *{box-sizing:border-box;margin:0;padding:0}
  html,body{width:1200px;height:1200px;overflow:hidden;background:var(--stage)}
  body{font-family:"Jost",sans-serif;color:var(--ink)}
  .page{position:absolute;left:220px;top:0;width:760px;height:1200px;background:var(--paper);overflow:hidden}

  .site-header{position:relative;height:250px;background:linear-gradient(160deg,var(--header-mid),var(--header-dark) 70%);}
  .utility-nav{position:absolute;top:22px;right:34px;display:flex;gap:10px;font-size:12px;letter-spacing:.08em;color:#d7dde6;text-transform:uppercase}
  .utility-nav span.sep{color:#7d8794}
  .brand{position:absolute;left:40px;top:78px;display:flex;align-items:center;gap:18px}
  .brand-dot{width:64px;height:64px;border-radius:50%;background:var(--brand-cyan)}
  .brand-name{font-size:58px;font-weight:500;color:var(--brand-cyan);letter-spacing:.01em}

  .main-nav{position:absolute;left:30px;bottom:18px;display:flex;gap:8px}
  .tab{width:108px;height:30px;line-height:26px;text-align:center;font-size:13px;letter-spacing:.08em;text-transform:uppercase;color:#dfe9f3;background:var(--tab-fill);border:2px solid var(--brand-cyan);border-radius:3px}
  .tab.is-active{background:var(--tab-active);color:#fff}

  .backdrop{position:absolute;left:0;top:250px;width:760px;height:950px;background:
      linear-gradient(115deg,var(--sky-pale) 0 18%,transparent 18% 70%,var(--sky-bright) 70% 82%,var(--sky-pale) 82%),
      linear-gradient(180deg,#eef5fb,#ffffff 40%,#e4f0f9)}
  .content{position:absolute;left:0;top:250px;width:760px;padding:0 70px}

  .section-title{font-weight:300;text-align:center;color:var(--ink)}
  .home-title{font-size:34px;margin-top:34px;letter-spacing:.03em}
  .lede{font-size:15px;line-height:1.35;text-align:center;margin-top:10px}
  .lede + .lede{margin-top:16px}

  .formula{display:flex;align-items:center;justify-content:center;gap:12px;margin-top:34px}
  .step{width:78px;height:78px;border-radius:50%;background:radial-gradient(circle at 40% 35%,#4a5058,var(--bubble) 70%);color:#fff;font-size:15px;display:flex;align-items:center;justify-content:center;box-shadow:0 0 0 3px #ffffff,0 0 0 4px #c9d3dd}
  .op{font-size:28px;font-weight:600}
  .result{font-size:26px;line-height:1.05;font-weight:400;text-align:center;margin-left:6px}

  .divider{width:300px;height:2px;background:var(--rule);margin:48px auto 0}

  .platform-title{font-size:74px;margin-top:40px;letter-spacing:.02em}
  .body-copy{font-size:15px;line-height:1.4;margin-top:16px}
  .list-intro{font-size:15px;margin-top:14px}
  .features{margin-top:8px;padding-left:38px;font-size:15px;line-height:1.4}
  .features li{margin-bottom:2px}
</style>
</head>
<body>
<div class="page">
  <header class="site-header">
    <nav class="utility-nav">
      <span>Login</span><span class="sep">|</span>
      <span>Support</span><span class="sep">|</span>
      <span>Contact</span><span class="sep">|</span>
      <span>Privacy Policy</span>
    </nav>
    <div class="brand">
      <span class="brand-dot"></span>
      <span class="brand-name">Brivanta</span>
    </div>
    <nav class="main-nav">
      <span class="tab is-active">Home</span>
      <span class="tab">Platform</span>
      <span class="tab">Partners</span>
      <span class="tab">Blog</span>
      <span class="tab">About</span>
      <span class="tab">Contact</span>
    </nav>
  </header>

  <div class="backdrop" role="img" aria-label="Large soft light-blue brand shapes behind the page content"></div>

  <main class="content">
    <h1 class="section-title home-title">HOME</h1>
    <p class="lede">Brivanta is company which provides specialized offerings in IoT domain. Based in the heart of the Silicon Valley, California. Brivanta is built on decades of experience and knowledge.</p>
    <p class="lede">Brivanta CX IoT platform for OEM's is designed to ease the transition of Product companies from selling unconnected products, into providing service for connected devices.</p>

    <div class="formula">
      <span class="step">Learn</span><span class="op">+</span>
      <span class="step">Connect</span><span class="op">+</span>
      <span class="step">Intigrate</span><span class="op">=</span>
      <span class="result">Connected<br>Product</span>
    </div>

    <div class="divider"></div>

    <h2 class="section-title platform-title">PLATFORM</h2>
    <p class="body-copy">Brivanta's customizable CX IoT platform for OEM's provides essential and complicated integrations to enable a connected product to be successfully launched.</p>
    <p class="list-intro">Particular integrations include:</p>
    <ul class="features">
      <li>Multi-tennant PaaS solution</li>
      <li>Abstract device models and multi product support</li>
      <li>Data integration from IoT Connected device clouds, such as Nimbara Cloud, Holvex, Tessago and others.</li>
      <li>Mobile Application infrastructure (SDK) to support rapid branded mobile Application development, including in-app notifications</li>
      <li>Business operations integration with systems such as ERP, CRM, and billing platforms.</li>
    </ul>
  </main>
</div>
</body>
</html>
```